Need Business Card for our Indian Grocery Store

Industry/Entity Type

Grocery Store

Contact Information for Business Card

Manoj Baweja
Director

Store Locations:

Kelbrook
482 Elm Parade
P: 03 9172 5843

Ashvale
613 Carlow Road
P: 03 9238 6014

email: kvtmarts@mailnest.example

Requirements
Must have
• Our logo Colours

```html
<!DOCTYPE html>
<html lang="en">
<head>
<meta charset="utf-8">
<title>KVT Marts – Business Card</title>
<link rel="stylesheet" href="https://fonts.googleapis.com/css2?family=Raleway:wght@400;500;600&display=swap">
<style>
  :root {
    --backdrop: #3d3f66;
    --brand-red: #e31e28;
    --card-white: #ffffff;
    --ink: #1a1a1a;
    --rule: #2a2a2a;
  }
  * { margin: 0; padding: 0; box-sizing: border-box; }
  html, body { width: 1200px; height: 1200px; overflow: hidden; }
  body {
    position: relative;
    background: var(--backdrop);
    font-family: "Raleway", sans-serif;
    color: var(--ink);
  }
  .card {
    position: absolute;
    width: 780px;
    height: 446px;
    border-radius: 40px;
  }
  .card-front {
    left: 126px; top: 114px;
    background: var(--brand-red);
    display: flex; align-items: center; justify-content: center;
  }
  .front-brand {
    color: var(--card-white);
    font-weight: 600;
    font-size: 92px;
    letter-spacing: 2px;
  }
  .card-back {
    left: 292px; top: 632px;
    background: var(--card-white);
  }
  .abs { position: absolute; }
  .person-name {
    left: 56px; top: 180px;
    font-size: 29px; font-weight: 600;
    white-space: nowrap;
  }
  .person-surname { color: var(--brand-red); }
  .person-role {
    left: 56px; top: 223px;
    font-size: 17px; font-weight: 500;
  }
  .back-brand {
    left: 56px; top: 330px;
    color: var(--brand-red);
    font-size: 38px; font-weight: 600;
    white-space: nowrap;
  }
  .divider-v {
    left: 294px; top: 42px;
    width: 1.5px; height: 368px;
    background: var(--rule);
  }
  .divider-h {
    left: 294px; width: 436px; height: 1.5px;
    background: var(--rule);
  }
  .section-title {
    left: 312px; top: 62px;
    font-size: 21px; font-weight: 500;
  }
  .contact-line {
    left: 392px;
    font-size: 22px; font-weight: 500;
    white-space: nowrap;
  }
  .icon { left: 351px; width: 22px; height: 22px; }
</style>
</head>
<body>
  <section class="card card-front">
    <div class="front-brand">KVT Marts</div>
  </section>

  <section class="card card-back">
    <div class="abs person-name">Manoj <span class="person-surname">Baweja</span></div>
    <div class="abs person-role">Director</div>
    <div class="abs back-brand">KVT Marts</div>

    <div class="abs divider-v"></div>
    <div class="abs section-title">Store Locations</div>
    <div class="abs divider-h" style="top:104px"></div>

    <svg class="abs icon" style="top:126px" viewBox="0 0 24 24" aria-hidden="true"><path d="M12 2a7 7 0 0 0-7 7c0 5 7 13 7 13s7-8 7-13a7 7 0 0 0-7-7zm0 9.5A2.5 2.5 0 1 1 12 6.5a2.5 2.5 0 0 1 0 5z" fill="#111"/></svg>
    <div class="abs contact-line" style="top:128px">Kelbrook,</div>
    <div class="abs contact-line" style="top:156px">482 Elm Parade</div>
    <svg class="abs icon" style="top:192px" viewBox="0 0 24 24" aria-hidden="true"><circle cx="12" cy="12" r="10" fill="none" stroke="#111" stroke-width="1.8"/><path d="M9 7.5l1.6 2.4-1 1.2c.7 1.4 1.8 2.5 3.2 3.2l1.2-1 2.4 1.6-.8 1.7c-3.6-.4-6.9-3.7-7.3-7.3z" fill="#111"/></svg>
    <div class="abs contact-line" style="top:191px">03 9172 5843</div>
    <div class="abs divider-h" style="top:226px"></div>

    <svg class="abs icon" style="top:247px" viewBox="0 0 24 24" aria-hidden="true"><path d="M12 2a7 7 0 0 0-7 7c0 5 7 13 7 13s7-8 7-13a7 7 0 0 0-7-7zm0 9.5A2.5 2.5 0 1 1 12 6.5a2.5 2.5 0 0 1 0 5z" fill="#111"/></svg>
    <div class="abs contact-line" style="top:249px">Ashvale,</div>
    <div class="abs contact-line" style="top:277px">613 Carlow Road</div>
    <svg class="abs icon" style="top:312px" viewBox="0 0 24 24" aria-hidden="true"><circle cx="12" cy="12" r="10" fill="none" stroke="#111" stroke-width="1.8"/><path d="M9 7.5l1.6 2.4-1 1.2c.7 1.4 1.8 2.5 3.2 3.2l1.2-1 2.4 1.6-.8 1.7c-3.6-.4-6.9-3.7-7.3-7.3z" fill="#111"/></svg>
    <div class="abs contact-line" style="top:311px">03 9238 6014</div>
    <div class="abs divider-h" style="top:349px"></div>

    <svg class="abs icon" style="top:368px;width:28px;left:348px" viewBox="0 0 28 20" aria-hidden="true"><rect x="1" y="2" width="26" height="16" fill="none" stroke="#111" stroke-width="1.8"/><path d="M1 2l13 10L27 2M1 18l10-8M27 18l-10-8" fill="none" stroke="#111" stroke-width="1.6"/></svg>
    <div class="abs contact-line" style="top:365px;left:398px">kvtmarts@mailnest.example</div>
  </section>
</body>
</html>
```